THE PRACTICE NAME "The Renal Crest MD" FOR A NEW MEDICAL PRACTICE STARTUP

THIS IS A BUSINESS CARD REQUEST FOR A KIDNEY DOCTOR's(NEPHROLOGIST) PRACTICE, THIS PRACTICE WILL BE IN EL PASO,TEXAS USA.OPEN TO INNOVATIVE IDEAS!

THE RENAL CREST MD ( NAME OF PRACTICE)

VIKRANT L. MOTHRE, MD FNKF FASN ( NAME OF PHYSICIAN WITH DEGREES)
BOARD CERTIFIED INTERNAL MEDICINE
BOARD CERTIFIED NEPHROLOGY
HYPERTENSION SPECIALIST

OFFICE ADDRESS, PHONE, FAX AND EMAIL PENDING

Guarding Health. Building Futures.(MOTTO) THE LOGO SHOILD REFLECT THIS MESSAGE. WE NEED A LOGO DESIGN WITH 2 KIDNEYS OR CAN BE ONE KIDNEY ALSO.

Target Market(s)

PATIENTS WITH KIDNEY DISEASE, HYPERTENSION, ENGLISH AND SPANISH SPEAKING POPULATION AND PATIENTS ON DIALYSIS

Industry/Entity Type

Health Care

Contact Information for Business Card

HYPERTENSION SPECIALIST

WEBSITE URL PENDING

Font styles to use
Serif
Sans Serif
Script

Colors
fbed38
ffc214
fbf289
fbee3e
5c5c5c
333333
1b1b1b
757575
d3d3d3

Requirements
Must have
• A KIDNEY LOGO
• NAME OF THE PRACTICE
Nice to have
• IF THE CARD CAN BE IN THE SHAPE OF A KIDNEY

```html
<!DOCTYPE html>
<html lang="en">
<head>
<meta charset="utf-8">
<title>The Renal Crest MD – Business Card</title>
<link rel="stylesheet" href="https://fonts.googleapis.com/css2?family=Open+Sans:ital,wght@0,400;0,700;0,800;1,700&display=swap">
<style>
  :root {
    --stage: #555555;
    --card: #000000;
    --accent: #00aeef;
    --ink-light: #ffffff;
    --ink-dark: #0a0a0a;
  }
  * { box-sizing: border-box; margin: 0; padding: 0; }
  html, body {
    width: 1200px;
    height: 999px;
    overflow: hidden;
    background: var(--stage);
    font-family: "Open Sans", Arial, sans-serif;
  }
  .business-card {
    position: absolute;
    left: 75px;
    top: 200px;
    width: 1050px;
    height: 600px;
    background: var(--card);
    border-radius: 0 95px 0 95px;
    overflow: hidden;
  }
  .brand {
    position: absolute;
    left: 48px;
    top: 112px;
    display: flex;
    align-items: center;
    gap: 18px;
  }
  .brand-mark {
    width: 100px;
    height: 100px;
    background: var(--accent);
  }
  .brand-name {
    color: var(--ink-light);
    font-weight: 800;
    font-size: 40px;
    line-height: 1;
    letter-spacing: 0.5px;
  }
  .brand-tagline {
    color: var(--accent);
    font-size: 22px;
    margin-top: 6px;
  }
  .physician {
    position: absolute;
    left: 90px;
    bottom: 62px;
    color: var(--ink-light);
  }
  .physician-name {
    font-weight: 700;
    font-style: italic;
    font-size: 33px;
    margin-bottom: 10px;
  }
  .credentials {
    list-style: none;
    font-size: 19px;
    line-height: 1.3;
  }
  .contact {
    position: absolute;
    left: 600px;
    top: 268px;
    right: 0;
  }
  .address {
    color: var(--ink-light);
    font-size: 21px;
    line-height: 1.35;
    margin-bottom: 18px;
  }
  .contact-row {
    display: flex;
    gap: 8px;
    height: 44px;
    margin-bottom: 12px;
  }
  .contact-icon {
    width: 44px;
    background: var(--accent);
    display: flex;
    align-items: center;
    justify-content: center;
  }
  .contact-icon svg { width: 26px; height: 26px; fill: var(--ink-dark); }
  .contact-value {
    flex: 1;
    background: var(--accent);
    color: var(--ink-dark);
    font-size: 21px;
    line-height: 44px;
    padding-left: 12px;
  }
</style>
</head>
<body>
  <section class="business-card">
    <div class="brand">
      <div class="brand-mark" aria-hidden="true"></div>
      <div>
        <p class="brand-name">THE RENAL CREST MD</p>
        <p class="brand-tagline">Guarding Health. Building Futures.</p>
      </div>
    </div>

    <div class="physician">
      <h1 class="physician-name">VIKRANT L. MOTHRE</h1>
      <ul class="credentials">
        <li>MD FNKF FASN</li>
        <li>BOARD CERTIFIED INTERNAL MEDICINE</li>
        <li>BOARD CERTIFIED NEPHROLOGY</li>
        <li>HYPERTENSION SPECIALIST</li>
      </ul>
    </div>

    <div class="contact">
      <p class="address">suit # 00, Lorem ipsum<br>Lorem Lorem ipsum</p>

      <div class="contact-row">
        <div class="contact-icon">
          <svg viewBox="0 0 24 24" aria-label="Phone"><path d="M6.6 10.8a15.1 15.1 0 0 0 6.6 6.6l2.2-2.2c.3-.3.7-.4 1-.2 1.1.4 2.3.6 3.6.6.6 0 1 .4 1 1V20c0 .6-.4 1-1 1A17 17 0 0 1 3 4c0-.6.4-1 1-1h3.5c.6 0 1 .4 1 1 0 1.3.2 2.5.6 3.6.1.3 0 .7-.2 1z"/></svg>
        </div>
        <div class="contact-value">000-000-0000</div>
      </div>

      <div class="contact-row">
        <div class="contact-icon">
          <svg viewBox="0 0 24 24" aria-label="Fax"><path d="M7 2h10v6H7z"/><path d="M4 9h16a1 1 0 0 1 1 1v8h-3v-4H6v4H3v-8a1 1 0 0 1 1-1z"/><path d="M7 15h10v7H7z"/></svg>
        </div>
        <div class="contact-value">000-000-0000</div>
      </div>

      <div class="contact-row">
        <div class="contact-icon">
          <svg viewBox="0 0 24 24" aria-label="Email"><path d="M2 6h20v13H2z" opacity="0"/><path d="M3 6h18v13H3zm2 2v.4l7 5 7-5V8z"/></svg>
        </div>
        <div class="contact-value">hello@renalcrestmd.com</div>
      </div>
    </div>
  </section>
</body>
</html>
```